Etikett-Design für Olivenöl
Unsere Vorgaben wurden gut aufgenommen. Der erste Entwurf hat uns sofort angesprochen. Wir hatten noch ein paar Modifikationen und das Projekt war sehr schnell erfolgreich abgeschlossen. Wir werden weitere Themen hier beauftragen. Besten Dank.
Zielgruppe
Einzelhandel. Die Zielgruppe ist 30 bis 55 Jahre alt, weiblich sowie männlich.
Aufgabenstellung
Das Label für die 100ml große Flasche soll 13,4 cm x 6,7 cm groß sein.
In der Flasche ist ein hochwertiges natives Olivenöl.
Das Design soll frisch, klar, ansprechend, anziehend und freundlich sein.

```html
<!DOCTYPE html>
<html lang="de">
<head>
<meta charset="utf-8">
<title>Olivenöl Etikett – Verdessa</title>
<link href="https://fonts.googleapis.com/css2?family=Poppins:wght@700;800&family=Open+Sans:wght@400;700&family=Caveat+Brush&display=swap" rel="stylesheet">
<style>
  :root {
    --olive-green: #7ab51d;
    --ink: #111111;
    --text: #222222;
    --heart-red: #c8102e;
    --label-white: #ffffff;
    --canvas-bg: #ececec;
    --muted-green: #e6f0d6;
  }
  * { margin: 0; padding: 0; box-sizing: border-box; }
  html, body {
    width: 1050px; height: 1200px; overflow: hidden;
    background: var(--canvas-bg);
  }
  .label {
    position: absolute; left: 40px; top: 357px;
    width: 970px; height: 485px;
    background: var(--label-white);
    box-shadow: 0 2px 10px rgba(0,0,0,0.08);
    font-family: "Open Sans", sans-serif;
    color: var(--text);
  }
  .label > * { position: absolute; }

  /* left column */
  .claim {
    left: 37px; top: 27px;
    font-family: "Poppins", sans-serif; font-weight: 800;
    font-size: 38px; line-height: 45px; color: var(--ink);
    letter-spacing: -0.5px;
  }
  .claim .accent { color: var(--olive-green); }
  .donation {
    left: 40px; top: 180px; width: 193px; height: 51px;
    border: 2px solid var(--olive-green);
    display: flex; align-items: center; gap: 10px; padding-left: 9px;
  }
  .donation::after {
    content: ""; position: absolute; left: 104px; bottom: -9px;
    width: 14px; height: 14px; background: var(--label-white);
    border-right: 2px solid var(--olive-green);
    border-bottom: 2px solid var(--olive-green);
    transform: skewX(35deg) rotate(45deg) scale(0.7);
  }
  .donation-text {
    font-weight: 700; font-size: 13.5px; line-height: 17px; color: var(--ink);
  }
  .storage {
    left: 38px; top: 404px;
    font-size: 15px; line-height: 18.5px; color: var(--ink);
  }

  /* center column */
  .brand-mark {
    left: 428px; top: 45px; width: 116px; height: 116px;
    border-radius: 50%; background: var(--olive-green);
  }
  .brand-name {
    left: 320px; width: 330px; top: 180px; text-align: center;
    font-weight: 700; font-size: 15px; color: var(--ink);
  }
  .product-name {
    left: 320px; width: 330px; top: 218px; text-align: center;
    font-family: "Poppins", sans-serif; font-weight: 700;
    font-size: 42px; line-height: 54px; color: var(--olive-green);
  }
  .grade {
    left: 320px; width: 330px; top: 268px; text-align: center;
    font-family: "Caveat Brush", cursive; font-size: 40px; line-height: 44px;
    color: var(--ink); letter-spacing: 0.5px;
  }
  .harvest {
    left: 320px; width: 330px; top: 315px; text-align: center;
    font-family: "Poppins", sans-serif; font-weight: 700;
    font-size: 18px; color: var(--olive-green);
  }
  .process {
    left: 320px; width: 330px; top: 356px; text-align: center;
    font-size: 15.5px; line-height: 19px; color: var(--text);
  }
  .facts {
    left: 345px; width: 325px; top: 441px;
    display: flex; justify-content: space-between; padding: 0 20px;
    font-weight: 700; font-size: 17px; color: var(--ink);
  }
  .accent-bar {
    left: 324px; width: 325px; top: 475px; height: 10px;
    background: var(--olive-green);
  }

  /* right column */
  .bottler {
    right: 42px; top: 25px; text-align: right;
    font-weight: 700; font-size: 17px; line-height: 22px; color: var(--ink);
  }
  .address {
    right: 42px; top: 90px; text-align: right; font-style: normal;
    font-size: 17.5px; line-height: 21.5px; color: var(--ink);
  }
  .email {
    right: 42px; top: 176px; font-size: 17.5px; color: var(--ink);
  }
  .nutrition {
    left: 711px; width: 217px; top: 232px; border-collapse: collapse;
    font-size: 12.5px; line-height: 16.4px; color: var(--ink);
  }
  .nutrition caption {
    text-align: right; font-weight: 700; font-size: 14.5px;
    padding-bottom: 3px; border-bottom: 1.5px solid var(--ink);
  }
  .nutrition td { padding: 0; }
  .nutrition td:last-child { text-align: right; white-space: nowrap; }
  .nutrition tr:first-child td { padding-top: 3px; }
  .nutrition .main td:first-child { font-weight: 700; }
  .variety {
    left: 711px; top: 398px;
    font-weight: 700; font-size: 12.5px; color: var(--ink);
  }
  .pairing-icons {
    left: 711px; top: 428px; width: 166px; height: 34px;
    border-radius: 17px; background: var(--muted-green);
  }
</style>
</head>
<body>
  <main class="label">
    <h1 class="claim">Kalt,<br><span class="accent">elegant &amp;</span><br>lecker.</h1>

    <div class="donation">
      <svg width="38" height="34" viewBox="0 0 38 34" aria-hidden="true">
        <path d="M19 33 C6 23 1 16 1 9.5 C1 4.5 5 1 9.8 1 C13.8 1 17 3.5 19 7 C21 3.5 24.2 1 28.2 1 C33 1 37 4.5 37 9.5 C37 16 32 23 19 33 Z" fill="var(--heart-red)"/>
      </svg>
      <p class="donation-text">Wir spenden vom<br>Verkaufserlös</p>
    </div>

    <p class="storage">Mindestens haltbar bis:<br>Siehe Flasche<br>Kühl und dunkel lagern</p>

    <div class="brand-mark" aria-hidden="true"></div>
    <p class="brand-name">VERDESSA - est 2009</p>
    <h2 class="product-name">Olivenöl</h2>
    <p class="grade">EXTRA NATIV</p>
    <p class="harvest">frühe Ernte</p>
    <p class="process">sortenrein &amp; mühlenfrisch<br>kaltgepresst</p>
    <div class="facts"><span>0,17% Ölsäure</span><span>250ml</span></div>
    <div class="accent-bar"></div>

    <p class="bottler">Abgefüllt von Almazara Sol<br>für Verdessa OHG</p>
    <address class="address">Lindenallee 14b<br>20259 Hamburg<br>Deutschland</address>
    <p class="email">info@verdessa.com</p>

    <table class="nutrition">
      <caption>Nährwerte pro 100ml</caption>
      <tr><td>Energie</td><td>3700 kj / 900 kcal</td></tr>
      <tr class="main"><td>Fett</td><td>100,0g</td></tr>
      <tr><td>davon gesättigte Fettsäuren</td><td>13,0g</td></tr>
      <tr class="main"><td>Kohlenhydrate</td><td>0,0g</td></tr>
      <tr><td>davon Zucker</td><td>0,0g</td></tr>
      <tr class="main"><td>Eiweiß</td><td>0,0g</td></tr>
      <tr><td>Salz</td><td>0,0g</td></tr>
    </table>

    <p class="variety">Sorte Arbequina, Ideal zu:</p>
    <div class="pairing-icons" role="img" aria-label="Symbole für Fisch, Salat, Gebäck und Brot in Grün"></div>
  </main>
</body>
</html>
```